ebook cover for The Heron & The Marigold (Zing!)

We would like an ebook cover for a post Ph.D. on Animal Totems book called The Heron and The Marigold. It is about human relationships and dating. Author is Marta Lindqvist Ph.D.
I am thinking perhaps just typographic with a fancy custom italicized or handwriting kind of font that fills the whole page, or a picture that doesn't belittle the fairytale of love. Something cosmic.
The subtitle to guide people, small, is "on dating"

```html
<!DOCTYPE html>
<html lang="en">
<head>
<meta charset="utf-8">
<title>The Heron and The Marigold — On Dating</title>
<link rel="stylesheet" href="https://fonts.googleapis.com/css2?family=Kaushan+Script&family=Arimo:wght@500&family=Tinos&display=swap">
<style>
  :root {
    --backdrop: #d9dee0;
    --cover-yellow: #fce200;
    --glow-green: #b2dc46;
    --title-orange: #e2621f;
    --title-pink: #e8697a;
    --ink: #161616;
  }
  * { margin: 0; padding: 0; box-sizing: border-box; }
  html, body {
    width: 1200px;
    height: 800px;
    overflow: hidden;
    background: var(--backdrop);
  }
  .canvas {
    position: relative;
    width: 1200px;
    height: 800px;
  }
  .cover {
    position: absolute;
    left: 340px;
    top: 20px;
    width: 520px;
    height: 760px;
    background:
      radial-gradient(ellipse 210px 150px at 50% 55%, var(--glow-green) 0%, rgba(178,220,70,0.55) 45%, rgba(252,226,0,0) 100%),
      var(--cover-yellow);
    box-shadow: 0 10px 30px rgba(0,0,0,0.12);
  }
  .line {
    position: absolute;
    left: 0;
    right: 0;
    text-align: center;
    white-space: nowrap;
  }
  .script {
    font-family: "Kaushan Script", cursive;
    line-height: 1;
  }
  .title-article-top {
    top: 82px;
    font-size: 58px;
    color: var(--title-orange);
    padding-left: 40px;
  }
  .title-heron {
    top: 140px;
    font-size: 128px;
    color: var(--title-orange);
  }
  .title-and {
    top: 285px;
    font-size: 58px;
    color: var(--ink);
  }
  .title-article-bottom {
    top: 355px;
    font-size: 66px;
    color: var(--title-pink);
  }
  .title-marigold {
    top: 415px;
    font-size: 100px;
    color: var(--title-pink);
  }
  .subtitle {
    top: 592px;
    font-family: "Arimo", sans-serif;
    font-weight: 500;
    font-size: 29px;
    letter-spacing: 4px;
    color: var(--ink);
  }
  .author {
    top: 686px;
    font-family: "Tinos", serif;
    font-size: 30px;
    letter-spacing: 2px;
    color: var(--ink);
  }
</style>
</head>
<body>
  <main class="canvas">
    <article class="cover">
      <h1>
        <span class="line script title-article-top">The</span>
        <span class="line script title-heron">Heron</span>
        <span class="line script title-and">and</span>
        <span class="line script title-article-bottom">The</span>
        <span class="line script title-marigold">Marigold</span>
      </h1>
      <p class="line subtitle">ON DATING</p>
      <p class="line author">Marta Lindqvist Ph.D.</p>
    </article>
  </main>
</body>
</html>
```